Wedding Company needs Brochure Design

FOR THIS PROJECT, WE ARE LOOKING FOR A BROCHURE. WHOEVER WE CHOOSE AS THE WINNING BROCHURE DESIGN WILL THEN DESIGN OUR WEBSITE AND BUSINESS CARD.

We're are looking to expand our brochure by making it a circle and adding 6 inside pages of information with a front and back cover. The pages will be as follows:

Front
About us
About us pictures
Wedding Planning
Wedding planning pictures
Lighting & Decor
Lighting & decor pictures
Back

We've uploaded a picture of our current brochure... so you can get an idea of what we've liked before. Please give us your creative input & design ideas. We've put together a "mock" brochure for you to take a look at as well. As you can see we need your help to properly lay out pictures so that the pages look full and the pictures pop and catches our clients attention.

A few words to describe our brochure would be "elegance", "class", "tasteful" and "colorful". We want to be able to portray that we are luxurious and innovative for the higher end brides and at the same time catering to the budget friendly brides.

Currently, we are waiting on a few pictures from the photographers and we are hoping to have them in a few days... In the meantime we've placed pictures we took from our phone as place holders.

Industry/Entity Type

Catering

```html
<!DOCTYPE html>
<html lang="en">
<head>
<meta charset="utf-8">
<title>Lighting and Decor – Brochure Spread</title>
<link href="https://fonts.googleapis.com/css2?family=Parisienne&family=Libre+Bodoni:wght@400;500;600&display=swap" rel="stylesheet">
<style>
  :root {
    --page-bg: #ffffff;
    --cream: #ede6d6;
    --gold: #a6852f;
    --gold-deep: #8d6b1e;
  }
  html, body {
    margin: 0;
    padding: 0;
    overflow: hidden;
    background: var(--page-bg);
  }
  .spread {
    position: relative;
    width: 1200px;
    height: 600px;
    overflow: hidden;
    background: var(--page-bg);
  }
  .info-page {
    position: absolute;
    left: 0;
    top: 0;
    width: 600px;
    height: 600px;
    border-radius: 50%;
    background: var(--cream);
  }
  .page-title {
    position: absolute;
    left: 0;
    top: 0;
    margin: 0;
    font-family: "Parisienne", cursive;
    font-weight: 400;
    color: var(--gold);
    font-size: 38px;
    line-height: 1;
  }
  .page-title .line-one {
    position: absolute;
    left: 210px;
    top: 132px;
    white-space: nowrap;
  }
  .page-title .line-two {
    position: absolute;
    left: 270px;
    top: 175px;
    white-space: nowrap;
  }
  .intro {
    position: absolute;
    left: 60px;
    top: 233px;
    width: 480px;
    margin: 0;
    font-family: "Libre Bodoni", serif;
    font-size: 11.6px;
    line-height: 20.3px;
    color: var(--gold-deep);
    text-align: center;
  }
  .services-lead {
    position: absolute;
    left: 60px;
    top: 333px;
    width: 480px;
    margin: 0;
    font-family: "Libre Bodoni", serif;
    font-size: 11.6px;
    color: var(--gold-deep);
    text-align: center;
  }
  .services {
    position: absolute;
    left: 80px;
    top: 357px;
    width: 440px;
    margin: 0;
    font-family: "Libre Bodoni", serif;
    font-weight: 600;
    font-size: 14px;
    line-height: 26.4px;
    letter-spacing: 0.1px;
    color: var(--gold);
    text-align: center;
    text-transform: uppercase;
  }
  .gallery-page {
    position: absolute;
    left: 600px;
    top: 0;
    width: 600px;
    height: 600px;
  }
</style>
</head>
<body>
<main class="spread">
  <section class="info-page">
    <h1 class="page-title">
      <span class="line-one">Lighting</span>
      <span class="line-two">and Decor</span>
    </h1>
    <p class="intro">
      Let our experts draw attention to your carefully chosen centerpieces, surround your<br>
      guests with your event colors and even write your initials in light. Looking for something<br>
      romantic? Imagine dining under lanterns and chandeliers. Ready to transform your event<br>
      to a hot dance club? Let our experts swirl and strobe light over your guests and dancefloor.
    </p>
    <p class="services-lead">We offer a wide range of lighting services including, but not limited to:</p>
    <p class="services">
      Pinspots * Staging * Intelligent Lighting<br>
      * Search Lights * Uplighting - Vinyl<br>
      * Special FX - Video Projection * Dance<br>
      Floors * Monograms * Draping<br>
      * Chiavari Chairs * Cafe Lights<br>
      * Custom Designs
    </p>
  </section>

  <section class="gallery-page">
    <svg width="600" height="600" viewBox="0 0 600 600" xmlns="http://www.w3.org/2000/svg">
      <defs>
        <clipPath id="gallery-circle">
          <circle cx="300" cy="300" r="283"/>
        </clipPath>
        <linearGradient id="g-group" x1="0" y1="0" x2="0" y2="1">
          <stop offset="0" stop-color="#2a1a3c"/>
          <stop offset="0.6" stop-color="#3b2650"/>
          <stop offset="1" stop-color="#c9b4e6"/>
        </linearGradient>
        <linearGradient id="g-tent" x1="0" y1="0" x2="0" y2="1">
          <stop offset="0" stop-color="#6f63d8"/>
          <stop offset="0.6" stop-color="#8a4fd0"/>
          <stop offset="1" stop-color="#2b2140"/>
        </linearGradient>
        <linearGradient id="g-drape" x1="0" y1="0" x2="1" y2="1">
          <stop offset="0" stop-color="#a64be0"/>
          <stop offset="0.6" stop-color="#6a3fd6"/>
          <stop offset="1" stop-color="#3d4fc4"/>
        </linearGradient>
        <linearGradient id="g-barn" x1="0" y1="0" x2="0" y2="1">
          <stop offset="0" stop-color="#4a3e7a"/>
          <stop offset="0.5" stop-color="#c07cb8"/>
          <stop offset="1" stop-color="#6a8ad0"/>
        </linearGradient>
        <linearGradient id="g-confetti" x1="0" y1="0" x2="0" y2="1">
          <stop offset="0" stop-color="#3a2a22"/>
          <stop offset="0.5" stop-color="#6b2a2a"/>
          <stop offset="1" stop-color="#2a1c1c"/>
        </linearGradient>
        <linearGradient id="g-floor" x1="0" y1="0" x2="0" y2="1">
          <stop offset="0" stop-color="#e6e8ef"/>
          <stop offset="1" stop-color="#c9ccd6"/>
        </linearGradient>
        <linearGradient id="g-teal" x1="0" y1="0" x2="0" y2="1">
          <stop offset="0" stop-color="#2a3a3c"/>
          <stop offset="0.5" stop-color="#2f8c93"/>
          <stop offset="1" stop-color="#5a4a3a"/>
        </linearGradient>
      </defs>

      <circle cx="300" cy="300" r="300" fill="var(--cream)"/>

      <g clip-path="url(#gallery-circle)">
        <rect x="0" y="0" width="600" height="600" fill="var(--cream)"/>
        <rect x="18" y="36" width="185" height="262" fill="url(#g-group)" role="img" aria-label="Photo: wedding party gathered on a lit dance floor"/>
        <rect x="18" y="302" width="185" height="263" fill="url(#g-barn)" role="img" aria-label="Photo: arched barn reception with chandeliers and coloured uplighting"/>
        <rect x="208" y="18" width="185" height="185" fill="url(#g-tent)" role="img" aria-label="Photo: tented reception with patterned ceiling light"/>
        <rect x="208" y="207" width="185" height="185" fill="url(#g-confetti)" role="img" aria-label="Photo: performers and guests under falling confetti"/>
        <rect x="208" y="396" width="185" height="186" fill="url(#g-floor)" role="img" aria-label="Photo: custom monogram dance floor with couple's names and date"/>
        <rect x="397" y="36" width="185" height="262" fill="url(#g-drape)" role="img" aria-label="Photo: purple draped ceremony stage with chandelier and floral arch"/>
        <rect x="397" y="302" width="185" height="263" fill="url(#g-teal)" role="img" aria-label="Photo: barn ceremony aisle with teal lighting and chandeliers"/>
      </g>
    </svg>
  </section>
</main>
</body>
</html>
```